Journeys With Marlowe Business Cards

I need a business card design for my upscale Travel Agency.
Attached you can find my logo.
I would like to include the following:
- Name
- Title
- Phone Number
- Email
- Website
- and then something like: Follow us: JourneysWithMarlowe (and then social media icons in color).
The logo should be in the front and then also the back.
I am also attaching a design that I liked (mostly for the layout) but open to any suggestions
Industry/Entity Type
Travel Agent
Contact Information for Business Card
Name: Celine Drummond
Title: Travel Designer / Owner
Phone: 415-296-0487
Email: celine@journeyswithmarlowe.example
Website: www.JourneysWithMarlowe.example
Social Media Handles for FB,IG, Twitter: JourneysWithMarlowe
Font styles to use
Colors
Designer to choose colors to be used in the design.
Look and feel

```html
<!DOCTYPE html>
<html lang="en">
<head>
<meta charset="utf-8">
<title>Journeys With Marlowe – Business Cards</title>
<link href="https://fonts.googleapis.com/css2?family=Open+Sans:wght@400;600;700&display=swap" rel="stylesheet">
<style>
  :root {
    --bg: #2b2b2d;
    --card: #ffffff;
    --orange: #f5a95a;
    --orange-deep: #f09a3e;
    --grey: #8a8a8a;
    --ink: #333333;
  }
  * { box-sizing: border-box; margin: 0; padding: 0; }
  html, body { width: 1200px; height: 900px; overflow: hidden; }
  body {
    background: var(--bg);
    font-family: "Open Sans", Arial, sans-serif;
    color: var(--ink);
    position: relative;
  }
  .card {
    position: absolute;
    left: 280px;
    width: 640px;
    height: 366px;
    background: var(--card);
    border-radius: 26px;
    overflow: hidden;
    box-shadow: 0 10px 30px rgba(0,0,0,0.45);
  }
  .card--front { top: 60px; }
  .card--back { top: 474px; }

  .brand {
    position: absolute;
    display: flex;
    align-items: center;
    gap: 14px;
    color: var(--orange-deep);
    font-weight: 600;
    white-space: nowrap;
  }
  .brand__mark {
    width: 34px;
    height: 34px;
    background: var(--orange);
  }
  .card--front .brand {
    left: 0; right: 0; top: 140px;
    justify-content: center;
    font-size: 34px;
  }
  .card--front .brand__mark { width: 44px; height: 44px; }
  .front-url {
    position: absolute;
    left: 0; right: 0; bottom: 34px;
    text-align: center;
    font-size: 15px;
    letter-spacing: 0.5px;
  }

  .card--back .brand {
    left: 34px; top: 128px;
    font-size: 22px;
    gap: 10px;
  }
  .card--back .brand__mark { width: 28px; height: 28px; }
  .divider {
    position: absolute;
    left: 322px; top: 70px;
    width: 2px; height: 190px;
    background: linear-gradient(to bottom, rgba(245,169,90,0), var(--orange) 30%, var(--orange) 70%, rgba(245,169,90,0));
    transform: rotate(14deg);
  }
  .contact {
    position: absolute;
    left: 352px; top: 62px;
  }
  .contact__name {
    color: var(--orange-deep);
    font-weight: 700;
    font-size: 24px;
    letter-spacing: 2px;
    text-transform: uppercase;
  }
  .contact__title {
    font-size: 14px;
    margin: 2px 0 12px;
    letter-spacing: 0.5px;
  }
  .contact__list { list-style: none; }
  .contact__item {
    display: flex;
    align-items: center;
    gap: 8px;
    font-size: 12.5px;
    line-height: 22px;
    white-space: nowrap;
  }
  .contact__icon { width: 14px; height: 14px; flex: none; }
  .contact__dot {
    width: 14px; height: 14px; border-radius: 50%;
    background: var(--orange); flex: none;
  }
  .wave {
    position: absolute;
    left: 0; bottom: 0;
    width: 640px; height: 140px;
  }
</style>
</head>
<body>
  <section class="card card--front">
    <div class="brand"><span class="brand__mark"></span>Journeys With Marlowe</div>
    <p class="front-url">www.JourneysWithMarlowe.example</p>
  </section>

  <section class="card card--back">
    <div class="brand"><span class="brand__mark"></span>Journeys With Marlowe</div>
    <div class="divider"></div>
    <div class="contact">
      <h1 class="contact__name">Celine Drummond</h1>
      <p class="contact__title">Travel Designer / Owner</p>
      <ul class="contact__list">
        <li class="contact__item">
          <svg class="contact__icon" viewBox="0 0 14 14"><circle cx="7" cy="7" r="7" fill="#f5a95a"/><path d="M4.5 3.8c.4-.3.9-.2 1.1.2l.6 1.1c.2.4 0 .8-.3 1 .4.9 1 1.5 1.9 1.9.2-.3.6-.5 1-.3l1.1.6c.4.2.5.7.2 1.1-.6.8-1.6.9-2.6.4-1.5-.8-2.6-1.9-3.4-3.4-.5-1-.4-2 .4-2.6z" fill="#fff"/></svg>
          415-296-0487
        </li>
        <li class="contact__item">
          <svg class="contact__icon" viewBox="0 0 14 14"><circle cx="7" cy="7" r="7" fill="#f5a95a"/><rect x="3.5" y="4.5" width="7" height="5" fill="none" stroke="#fff" stroke-width="1"/><path d="M3.5 4.5L7 7.3 10.5 4.5" fill="none" stroke="#fff" stroke-width="1"/></svg>
          celine@journeyswithmarlowe.example
        </li>
        <li class="contact__item">
          <svg class="contact__icon" viewBox="0 0 14 14"><circle cx="7" cy="7" r="7" fill="#f5a95a"/><circle cx="7" cy="7" r="3.6" fill="none" stroke="#fff" stroke-width="1"/><path d="M3.4 7h7.2M7 3.4c-1.5 2-1.5 5.2 0 7.2M7 3.4c1.5 2 1.5 5.2 0 7.2" fill="none" stroke="#fff" stroke-width=".8"/></svg>
          www.JourneysWithMarlowe.example
        </li>
        <li class="contact__item">
          <span class="contact__dot"></span>
          JourneysWithMarlowe
        </li>
      </ul>
    </div>
    <svg class="wave" viewBox="0 0 640 140" preserveAspectRatio="none">
      <path d="M0 40 C 140 120, 300 120, 420 112 C 520 106, 600 112, 640 130" fill="none" stroke="var(--grey)" stroke-width="5"/>
      <path d="M0 52 C 140 128, 300 128, 420 120 C 520 114, 600 120, 640 138 L640 140 L0 140 Z" fill="var(--orange)"/>
    </svg>
  </section>
</body>
</html>
```